Kelvora IT company focused on 3 areas of IT

Looking for something similar to attached cards. Logo for kelvora also attached.. Looking for something clean as far as colors (surprise me).. kelvo stands for 3 primary areas, web design, consulting and network infrastructure design. Please email me if you have any questions. Looking forward to seeing how creative and professional this card will look. Thank you,

Target Market(s)

Small business/consumers looking for It services

Industry/Entity Type

It Service

Contact Information for Business Card

Dorian Vesk
Principal Consultant

555-555-0173

www.kelvora-example.com
dvesk@kelvora-example.com

4172 Marsh Lantern Ct,
Ashvale, KV 00000

Colors

Designer to choose colors to be used in the design.

Requirements
Must have
• attached Logo design. Feel free to play with the colors.. If you have a better idea for a card, please fee free to send me. Looking for something clean/modern. Should have tech feel, not cheesy.
Nice to have
• Surprise me :-)..

```html
<!DOCTYPE html>
<html lang="en">
<head>
<meta charset="utf-8">
<title>Kelvora Business Card</title>
<link rel="stylesheet" href="https://fonts.googleapis.com/css2?family=Work+Sans:wght@400;500;600&display=swap">
<style>
  :root {
    --backdrop: #2a2a2c;
    --card: #1b1b1d;
    --accent: #1fa3e3;
    --ink: #ffffff;
    --ink-soft: #e6e6e6;
  }
  * { box-sizing: border-box; margin: 0; padding: 0; }
  html, body {
    width: 1200px; height: 900px; overflow: hidden;
    background: var(--backdrop);
    font-family: "Work Sans", Arial, sans-serif;
  }
  .stage {
    width: 1200px; height: 900px;
    display: flex; flex-direction: column; align-items: center; justify-content: center;
    gap: 44px;
  }
  .card {
    position: relative;
    width: 700px; height: 400px;
    background: var(--card);
    border-bottom: 7px solid var(--accent);
    box-shadow: 0 14px 30px rgba(0,0,0,0.45);
    overflow: hidden;
  }
  .brand {
    display: flex; align-items: center; gap: 14px;
    color: var(--ink);
    font-weight: 600;
    letter-spacing: 1px;
  }
  .brand-square { width: 22px; height: 22px; background: var(--accent); flex: none; }
  .card-front { display: flex; align-items: center; justify-content: center; }
  .card-front .brand { font-size: 64px; }
  .card-front .brand-square { width: 36px; height: 36px; }

  .card-back .brand {
    position: absolute; left: 50px; top: 168px;
    font-size: 42px;
  }
  .divider {
    position: absolute; left: 318px; top: 100px;
    width: 2px; height: 180px; background: var(--ink);
  }
  .details {
    position: absolute; left: 352px; top: 96px;
    color: var(--ink-soft);
  }
  .person-name {
    color: var(--accent);
    font-size: 34px; font-weight: 500; letter-spacing: 0.5px; line-height: 1.05;
  }
  .person-title { font-size: 18px; margin-bottom: 14px; letter-spacing: 0.5px; }
  .address { font-size: 18px; line-height: 1.3; margin-bottom: 10px; letter-spacing: 0.5px; }
  .contact-list { list-style: none; font-size: 18px; line-height: 1.45; letter-spacing: 0.5px; }
  .contact-list li { display: flex; align-items: center; gap: 10px; }
  .contact-icon { width: 13px; height: 13px; flex: none; }
</style>
</head>
<body>
<main class="stage">
  <section class="card card-front">
    <div class="brand"><span class="brand-square"></span>Kelvora</div>
  </section>

  <section class="card card-back">
    <div class="brand"><span class="brand-square"></span>Kelvora</div>
    <div class="divider"></div>
    <div class="details">
      <h1 class="person-name">DORIAN VESK</h1>
      <p class="person-title">Principal Consultant</p>
      <p class="address">4172 Marsh Lantern Ct,<br>Ashvale, KV 00000</p>
      <ul class="contact-list">
        <li>
          <svg class="contact-icon" viewBox="0 0 16 16"><path d="M4 1 L6.5 4.5 L5 6.5 Q6.5 9.5 9.5 11 L11.5 9.5 L15 12 L13 15 Q6 14 1 3 Z" fill="none" stroke="#1fa3e3" stroke-width="1.5" stroke-linejoin="round"/></svg>
          555-555-0173
        </li>
        <li>
          <svg class="contact-icon" viewBox="0 0 16 16"><rect x="1" y="3" width="14" height="10" fill="none" stroke="#1fa3e3" stroke-width="1.5"/><path d="M1 3 L8 9 L15 3" fill="none" stroke="#1fa3e3" stroke-width="1.5"/></svg>
          dvesk@kelvora-example.com
        </li>
        <li>
          <svg class="contact-icon" viewBox="0 0 16 16"><circle cx="8" cy="8" r="6.5" fill="none" stroke="#1fa3e3" stroke-width="1.4"/><ellipse cx="8" cy="8" rx="3" ry="6.5" fill="none" stroke="#1fa3e3" stroke-width="1.2"/><path d="M1.5 8 H14.5" stroke="#1fa3e3" stroke-width="1.2"/></svg>
          www.kelvora-example.com
        </li>
      </ul>
    </div>
  </section>
</main>
</body>
</html>
```